Business Card Design Project

I am a Homoeopath and would like a new business card which represents my clinic and how I work...My clinic Thistle Wellness is situated near Calderwood forest, you can hear the lyrebirds calling all the time!
My work is holistic and deals with shifting energy in order to create balance within the body. There is a very strong spiritual element to my work.
I have uploaded my current card, As far as the actual details on the front and the back I would like these to remain in the same structure...

Target Market(s)

those looking for alternative health therapies... all of my patients are referred to me so I am not concerned about fitting into a mainstream box

Industry/Entity Type

Clinic

Requirements
Must have
• This card must not look corporate!
be creative and different

Nice to have
• I am picturing a tree of life with roots heading into the earth and on it is a white peacock, maybe a body of water and a full moon nearby?

```html
<!DOCTYPE html>
<html lang="en">
<head>
<meta charset="utf-8">
<title>Helena Marsh – Classical Homoeopath business card</title>
<link rel="stylesheet" href="https://fonts.googleapis.com/css2?family=Alegreya:wght@700&family=EB+Garamond&family=Open+Sans:wght@400&display=swap">
<style>
  :root {
    --page: #ffffff;
    --leaf-strong: #8cc63f;
    --leaf-soft: #cfe4ad;
    --leaf-pale: #eef5e2;
    --name-dark: #2c4a14;
    --name-light: #4f7a2a;
    --name-back: #1b8a1b;
    --title-green: #2a7a4a;
    --credential-green: #1f6b2a;
    --card-grey-top: #f0f0f0;
    --card-grey-bottom: #cbcbcb;
    --card-edge: #a8a8a8;
    --rule-dark: #3a3a3a;
    --divider: #777777;
    --text-dark: #222222;
    --icon-blue: #2f5f95;
    --label: #111111;
  }
  * { box-sizing: border-box; margin: 0; padding: 0; }
  html, body { width: 1200px; height: 900px; overflow: hidden; background: var(--page); }
  .canvas { position: relative; width: 1200px; height: 900px; }

  .side-label {
    position: absolute; left: 26px;
    font: 400 26px "Open Sans", sans-serif; color: var(--label);
  }
  .side-label--front { top: 254px; }
  .side-label--back { top: 594px; left: 34px; }

  /* Front card */
  .card-front {
    position: absolute; left: 163px; top: 54px; width: 730px; height: 374px;
    border-radius: 14px 0 0 14px; overflow: hidden;
    background: linear-gradient(90deg, var(--leaf-strong) 0%, var(--leaf-soft) 45%, var(--leaf-pale) 75%, #ffffff 100%);
  }
  .card-front .leaf-art {
    position: absolute; left: 390px; top: 60px; width: 340px; height: 314px;
    background: radial-gradient(ellipse at 60% 70%, rgba(140,198,63,0.55) 0%, rgba(160,210,110,0.35) 45%, rgba(255,255,255,0) 75%);
  }
  .front-name {
    position: absolute; left: 25px; top: 76px;
    font: 700 55px/1 "Alegreya", serif; letter-spacing: 0.5px;
    background: linear-gradient(180deg, var(--name-light), var(--name-dark));
    -webkit-background-clip: text; background-clip: text; color: transparent;
  }
  .front-rule {
    position: absolute; left: 25px; top: 135px; width: 362px; height: 1px;
    background: rgba(60,90,30,0.35);
  }
  .front-title {
    position: absolute; left: 25px; top: 139px;
    font: 400 31px/1 "Open Sans", sans-serif; letter-spacing: 2px; color: var(--title-green);
  }
  .front-credentials {
    position: absolute; left: 37px; top: 168px;
    font: 400 19px/1 "EB Garamond", serif; color: var(--credential-green);
  }

  /* Back card */
  .card-back {
    position: absolute; left: 165px; top: 442px; width: 778px; height: 396px;
    border: 1px solid var(--card-edge); border-radius: 12px;
    background: linear-gradient(180deg, var(--card-grey-top), var(--card-grey-bottom));
  }
  .back-identity { position: absolute; left: 30px; top: 108px; }
  .back-name {
    font: 700 44px/1 "Alegreya", serif; color: var(--name-back); letter-spacing: 0.5px;
  }
  .back-rule {
    margin: 10px 0 0 5px; width: 286px; height: 1px; background: var(--rule-dark);
  }
  .back-title {
    margin: 10px 0 0 0;
    font: 400 24.5px/1 "Open Sans", sans-serif; letter-spacing: 1.6px; color: var(--title-green);
  }
  .back-credentials {
    margin: 3px 0 0 15px;
    font: 400 14px/1 "EB Garamond", serif; color: var(--credential-green);
  }
  .back-divider {
    position: absolute; left: 351px; top: 103px; width: 1px; height: 226px; background: var(--divider);
  }
  .contact-list { position: absolute; left: 366px; top: 121px; list-style: none; }
  .contact-item {
    display: flex; align-items: center; gap: 8px; height: 38px;
    font: 400 20px/1 "Open Sans", sans-serif; color: var(--text-dark);
  }
  .contact-icon { width: 22px; height: 22px; flex: none; fill: var(--icon-blue); }
</style>
</head>
<body>
<main class="canvas">
  <p class="side-label side-label--front">Front</p>
  <section class="card-front" aria-label="Business card front">
    <div class="leaf-art" role="img" aria-label="Two large soft green sprouting leaves"></div>
    <h1 class="front-name">Helena Marsh</h1>
    <div class="front-rule"></div>
    <p class="front-title">Classical Homoeopath</p>
    <p class="front-credentials">Adv Dip Hom Full Memb HPA Regd Prac</p>
  </section>

  <p class="side-label side-label--back">Back</p>
  <section class="card-back" aria-label="Business card back">
    <div class="back-identity">
      <h2 class="back-name">Helena Marsh</h2>
      <div class="back-rule"></div>
      <p class="back-title">Classical Homoeopath</p>
      <p class="back-credentials">Adv Dip Hom Full Memb HPA Regd Prac</p>
    </div>
    <div class="back-divider"></div>
    <ul class="contact-list">
      <li class="contact-item">
        <svg class="contact-icon" viewBox="0 0 24 24" aria-hidden="true"><circle cx="14" cy="7" r="5"/><path d="M11 10 L4 21 L6 21 L13 12 Z"/></svg>
        48 Wattle Lane, Bellmere
      </li>
      <li class="contact-item">
        <svg class="contact-icon" viewBox="0 0 24 24" aria-hidden="true"><path d="M2 8 Q12 2 22 8 L20 11 L16 10 L16 8 Q12 7 8 8 L8 10 L4 11 Z"/><path d="M6 12 L18 12 L21 20 L3 20 Z"/><circle cx="12" cy="16" r="2.2" fill="#fff"/></svg>
        03 5123 4870
      </li>
      <li class="contact-item">
        <svg class="contact-icon" viewBox="0 0 24 24" aria-hidden="true"><path d="M2 8 Q12 2 22 8 L20 11 L16 10 L16 8 Q12 7 8 8 L8 10 L4 11 Z"/><path d="M6 12 L18 12 L21 20 L3 20 Z"/><circle cx="12" cy="16" r="2.2" fill="#fff"/></svg>
        0412 555 309
      </li>
      <li class="contact-item">
        <svg class="contact-icon" viewBox="0 0 24 24" aria-hidden="true"><rect x="1" y="6" width="22" height="13"/><path d="M1 6 L12 14 L23 6" fill="none" stroke="#fff" stroke-width="1.5"/></svg>
        helena_marsh@fernmail.com
      </li>
    </ul>
  </section>
</main>
</body>
</html>
```